Course Graduation Certificate

This project is not for a flyer but instead for the creation of a course graduation certificate. The final certificate needs to include the Marlowe Summit Aviation Academy logo and the text stating as follows:
Certifies that ___________________________ has satisfactorily completed the course of _______________________________ on ________________________________
I would also like to include some type of gold seal of completion as well as a place to sign my name and credentials at the bottom of the certificate
I have included the Marlowe Summit Aviation Academy logo as well as three other certificate examples for you to work from.
Target Market(s)
Students completing a certification course and receiving a certificate
Look and feel

```html
<!DOCTYPE html>
<html lang="en">
<head>
<meta charset="utf-8">
<title>Certificate of Graduation</title>
<link rel="stylesheet" href="https://fonts.googleapis.com/css2?family=Alice&family=UnifrakturCook:wght@700&display=swap">
<style>
  :root {
    --paper: #f2ece2;
    --paper-shade: #e9e1d3;
    --navy: #0f2a47;
    --ornament-blue: #1a5fc0;
    --gold: #d2a03a;
    --ink: #1b1b1b;
    --seal-red: #d8383a;
    --seal-ring: #e84a44;
    --ribbon-red: #ee4140;
  }
  * { margin: 0; padding: 0; box-sizing: border-box; }
  html, body {
    width: 1200px; height: 848px; overflow: hidden;
    background: var(--paper);
  }
  .certificate {
    position: relative; width: 1200px; height: 848px;
    background: radial-gradient(ellipse at 50% 50%, var(--paper) 55%, var(--paper-shade) 100%);
    font-family: "Alice", Georgia, serif;
    color: var(--ink);
  }
  .frame, .seal { position: absolute; left: 0; top: 0; }
  .corner-ornament {
    position: absolute; width: 200px; height: 200px;
    background: radial-gradient(circle at var(--cx) var(--cy), rgba(26,95,192,.55) 0%, rgba(26,95,192,.25) 40%, rgba(26,95,192,0) 72%);
  }
  .corner-ornament.top-left { left: 82px; top: 85px; --cx: 12%; --cy: 12%; }
  .corner-ornament.top-right { right: 82px; top: 85px; --cx: 88%; --cy: 12%; }
  .corner-ornament.bottom-left { left: 82px; bottom: 85px; --cx: 12%; --cy: 88%; }
  .corner-ornament.bottom-right { right: 82px; bottom: 85px; --cx: 88%; --cy: 88%; }
  .side-ornament {
    position: absolute; top: 295px; width: 54px; height: 260px;
    background: radial-gradient(ellipse at 50% 50%, rgba(26,95,192,.45) 0%, rgba(26,95,192,.15) 55%, rgba(26,95,192,0) 75%);
  }
  .side-ornament.left { left: 83px; }
  .side-ornament.right { right: 83px; }
  .title {
    position: absolute; left: 0; width: 1200px; top: 132px;
    text-align: center;
    font-family: "UnifrakturCook", "Times New Roman", serif;
    font-weight: 700; font-size: 76px; line-height: 1;
    color: var(--gold);
  }
  .divider { position: absolute; left: 366px; top: 255px; width: 474px; height: 28px; }
  .divider-flourish {
    position: absolute; left: 78px; top: 6px; width: 318px; height: 16px; border-radius: 8px;
    background: linear-gradient(90deg, rgba(15,42,71,.2), rgba(15,42,71,.85) 50%, rgba(15,42,71,.2));
  }
  .intro {
    position: absolute; left: 0; width: 1190px; top: 297px;
    text-align: center; font-size: 31px; letter-spacing: 1px;
  }
  .fill-line { position: absolute; height: 0; border-top: 1.2px solid var(--ink); }
  .fill-line.recipient { left: 359px; width: 526px; top: 388px; }
  .fill-line.course { left: 603px; width: 437px; top: 461px; }
  .fill-line.date { left: 208px; width: 432px; top: 523px; }
  .statement { position: absolute; left: 153px; font-size: 21.5px; letter-spacing: .8px; }
  .statement.course-line { top: 440px; }
  .statement.date-line { top: 497px; }
  .academy-name {
    position: absolute; left: 243px; top: 640px; width: 243px;
    text-align: center; font-size: 21px; line-height: 1.2;
    color: var(--ornament-blue);
  }
  .signature-line { position: absolute; left: 764px; width: 174px; top: 642px; border-top: 2.5px solid var(--navy); }
  .signatory {
    position: absolute; right: 262px; top: 648px; text-align: right;
    font-size: 17.5px; line-height: 24px; letter-spacing: .8px;
  }
  .signatory-name {
    font-family: "UnifrakturCook", "Times New Roman", serif; font-weight: 700;
    font-size: 21px; letter-spacing: 0;
  }
</style>
</head>
<body>
<main class="certificate">
  <svg class="frame" width="1200" height="848" viewBox="0 0 1200 848" aria-hidden="true">
    <path d="M111 67 H1089 A45 45 0 0 0 1134 112 V736 A45 45 0 0 0 1089 781 H111 A45 45 0 0 0 66 736 V112 A45 45 0 0 0 111 67 Z" fill="none" stroke="var(--navy)" stroke-width="5"/>
    <path d="M120 76 H1080 A54 54 0 0 0 1125 121 V727 A54 54 0 0 0 1080 772 H120 A54 54 0 0 0 75 727 V121 A54 54 0 0 0 120 76 Z" fill="none" stroke="var(--navy)" stroke-width="1.5"/>
  </svg>

  <div class="corner-ornament top-left" role="img" aria-label="Blue floral corner ornament"></div>
  <div class="corner-ornament top-right" role="img" aria-label="Blue floral corner ornament"></div>
  <div class="corner-ornament bottom-left" role="img" aria-label="Blue floral corner ornament"></div>
  <div class="corner-ornament bottom-right" role="img" aria-label="Blue floral corner ornament"></div>
  <div class="side-ornament left" role="img" aria-label="Blue floral side ornament"></div>
  <div class="side-ornament right" role="img" aria-label="Blue floral side ornament"></div>

  <h1 class="title">Certificate of Graduation</h1>

  <div class="divider">
    <svg width="474" height="28" viewBox="0 0 474 28" aria-hidden="true">
      <line x1="0" y1="14" x2="474" y2="14" stroke="var(--navy)" stroke-width="2.5"/>
    </svg>
    <div class="divider-flourish" role="img" aria-label="Navy scroll flourish"></div>
  </div>

  <p class="intro">This Certifies that</p>
  <div class="fill-line recipient"></div>

  <p class="statement course-line">has satisfactorily completed the course of</p>
  <div class="fill-line course"></div>

  <p class="statement date-line">on</p>
  <div class="fill-line date"></div>

  <p class="academy-name">Marlowe Summit<br>Aviation Academy</p>

  <svg class="seal" width="1200" height="848" viewBox="0 0 1200 848" aria-hidden="true">
    <polygon points="572,690 556,722 572,718 582,734 598,700" fill="var(--ribbon-red)"/>
    <polygon points="622,690 638,722 622,718 612,734 596,700" fill="var(--ribbon-red)"/>
    <circle cx="597" cy="664" r="40" fill="var(--seal-ring)"/>
    <circle cx="597" cy="664" r="30" fill="var(--seal-red)"/>
  </svg>

  <div class="signature-line"></div>
  <div class="signatory">
    <p class="signatory-name">Elena Voss</p>
    <p>Project Manager</p>
    <p>Brightwell &amp; Partners</p>
  </div>
</main>
</body>
</html>
```